letterhead design

We have a business card with logo, ink etc and want to develop letterhead that uses the elements of the business card logo.
Must haves...and they should be designed in, not just plopped in :)
Dr. Lyle Varden
2817 W Marlow Street
Fresno, CA 93614
559-382-6157 p
559-382-7043 f
info@brindlespine.com
www.brindlespine.com
www.facebook.com/brindlespn
Updates

Rather than just have the logo on the page, is there someway to silkscreen it in the background to fill the page?

Reason: I was out of town for a week.

Industry/Entity Type

Business

Requirements
Nice to have
• I'd like the logo somehow silk screened in the background of the paper as well.

```html
<!DOCTYPE html>
<html lang="en">
<head>
<meta charset="utf-8">
<title>Brindle Spine Letterhead</title>
<link rel="stylesheet" href="https://fonts.googleapis.com/css2?family=Questrial&display=swap">
<style>
  :root {
    --backdrop: #2b2b2b;
    --paper: #ffffff;
    --ink-dark: #2a2624;
    --ink-light: #ffffff;
    --rule: #1e1e1e;
    --watermark: #dedede;
  }
  html, body {
    margin: 0;
    padding: 0;
    width: 1200px;
    height: 900px;
    overflow: hidden;
    background: var(--backdrop);
  }
  .canvas {
    position: relative;
    width: 1200px;
    height: 900px;
  }
  .letterhead {
    position: absolute;
    left: 283px;
    top: 40px;
    width: 634px;
    height: 820px;
    background: var(--paper);
    font-family: "Questrial", "Century Gothic", sans-serif;
    box-shadow: 0 6px 24px rgba(0,0,0,0.45);
    overflow: hidden;
  }
  .header-band {
    position: absolute;
    left: 0;
    top: 0;
    width: 634px;
    height: 190px;
  }
  .header-band .band-fill { fill: var(--ink-dark); }
  .header-band .band-line {
    fill: none;
    stroke: var(--ink-light);
    stroke-width: 3;
  }
  .contact-block {
    position: absolute;
    left: 0;
    top: 30px;
    width: 634px;
    text-align: center;
    color: var(--ink-light);
    font-size: 11px;
    line-height: 15px;
    letter-spacing: 0.3px;
  }
  .contact-block p { margin: 0; }
  .social-line::before {
    content: "";
    display: inline-block;
    width: 9px;
    height: 9px;
    margin-right: 5px;
    background: var(--ink-light);
    vertical-align: -1px;
  }
  .watermark-mark {
    position: absolute;
    left: 0;
    top: 300px;
    width: 634px;
    text-align: center;
    color: var(--watermark);
    font-size: 64px;
    line-height: 70px;
    letter-spacing: 2px;
  }
  .watermark-mark p { margin: 0; }
  .footer-rule {
    position: absolute;
    left: 40px;
    right: 40px;
    top: 748px;
    height: 0;
    border-top: 2px solid var(--rule);
  }
  .footer-web {
    position: absolute;
    left: 0;
    top: 764px;
    width: 634px;
    text-align: center;
    font-size: 22px;
    font-weight: 700;
    color: var(--rule);
    letter-spacing: 0.5px;
  }
</style>
</head>
<body>
<div class="canvas">
  <div class="letterhead">
    <svg class="header-band" viewBox="0 0 634 190" aria-hidden="true">
      <path class="band-fill" d="M0 0 H634 V190 H600 C585 190 580 178 565 170 C550 162 540 160 520 160 H114 C94 160 84 162 69 170 C54 178 49 190 34 190 H0 Z"/>
      <path class="band-line" d="M0 180 H30 C45 180 50 168 64 160 C80 152 92 150 114 150 H520 C542 150 554 152 570 160 C584 168 589 180 604 180 H634"/>
    </svg>
    <div class="contact-block">
      <p>Dr. Lyle Varden</p>
      <p>2817 W Marlow Street</p>
      <p>Alder Falls, CA 93614</p>
      <p>P: 555-382-6157</p>
      <p>F: 555-382-7043</p>
      <p>info@brindlespine.com</p>
      <p class="social-line">www.fernlink.net/brindlespn</p>
    </div>
    <div class="watermark-mark" aria-label="Brindle Spine Wellness Center">
      <p>Brindle Spine</p>
      <p>Wellness Center</p>
    </div>
    <div class="footer-rule"></div>
    <div class="footer-web">www.brindlespine.com</div>
  </div>
</div>
</body>
</html>
```